Lorcan Webpage Design

I would like to start an business and management consultancy business. I am thinking to called it "Movara Consultancy". Besides the consultancy services, I would also like to provide training on finance, forensic accounting, fraud prevention and internal control.
Professional management consultants are contracted by organizations to provide advisory services in an objective and independent manner.

Services include, but are not limited to, strategic planning, facilitation, quality assurance, education and training, investment counsel, identification and analysis of management problems, developing solutions, and the implementation of proposed solutions.

Professional management consultants are hired when an organization lacks sufficient resources, requires external objective advice, or because they have expertise not available within the client organization.

I would like to see the webpage design that use colors apple green with some other contrast color. The design have to be professional look but with a new age touch.

Reason: Unable to find a suitable web pages design

Dear all

Since last week I post a request, but till to date, I has yet to received a new sparkling creative and "wow" web page design. Please help me here!

Regards

Reason: Yet to found a suitable web designer for my web design. Help! I just need a fresh and professional look design. You may ignore the color code I prefer. Send me your sparkling creative work. Thank you so much!

Some examples

```html
<!DOCTYPE html>
<html lang="en">
<head>
<meta charset="utf-8">
<title>Movara Consultancy</title>
<link href="https://fonts.googleapis.com/css2?family=Arimo:wght@400;700&family=Arvo:wght@700&family=Oswald:wght@500&family=Raleway:ital,wght@0,400;0,500;1,400&family=Roboto+Condensed:wght@400;700&display=swap" rel="stylesheet">
<style>
:root{
  --green:#6cb212;
  --green-bright:#8fd61e;
  --green-dark:#4f8c0a;
  --black:#141414;
  --grey-bg:#ececec;
  --grey-line:#d6d6d6;
  --text:#555555;
  --text-dark:#222222;
  --blue:#1f7fc4;
  --white:#ffffff;
  --nav-active:#f2e21a;
}
*{margin:0;padding:0;box-sizing:border-box}
html,body{width:896px;height:1200px;overflow:hidden;background:var(--white)}
body{position:relative;font-family:'Raleway',sans-serif;color:var(--text)}
.abs{position:absolute}

/* header */
.site-header{position:absolute;left:0;top:0;width:896px;height:62px;background:linear-gradient(#2e2e2e,var(--black));border-bottom:2px solid var(--green)}
.logo-tab{position:absolute;left:0;top:0}
.logo-text{position:absolute;left:106px;top:6px;font-family:'Roboto Condensed',sans-serif;font-weight:700;font-size:24px;line-height:25px;color:var(--white);text-transform:uppercase}
.main-nav{position:absolute;top:26px;left:415px;display:flex;font-family:'Arimo',sans-serif;font-weight:700;font-size:11px;color:var(--white)}
.main-nav .n1{width:64px;color:var(--nav-active)}
.main-nav .n2{width:73px}
.main-nav .n3{width:89px}
.main-nav .n4{width:81px}

/* hero */
.hero{position:absolute;left:0;top:64px;width:896px;height:352px;overflow:hidden}
.hero-photo{position:absolute;inset:0;background:radial-gradient(ellipse at 78% 50%,#5a5f66 0%,#2e3033 40%,#1b1b1b 100%),#222}
.hero-title{position:absolute;left:106px;top:126px;color:var(--white)}
.hero-title .line1{font-family:'Arvo',serif;font-weight:700;font-size:37px;line-height:42px;letter-spacing:0.5px}
.hero-title .line1 .hl{background:var(--green);padding:0 6px 0 4px}
.hero-title .line2{font-family:'Oswald',sans-serif;font-weight:500;font-size:46px;line-height:54px;letter-spacing:0.3px}
.hero-arrow{position:absolute;left:0;top:0}

/* welcome */
.welcome{position:absolute;left:0;top:416px;width:896px;height:380px;background:var(--grey-bg)}
.welcome-title{position:absolute;top:16px;width:896px;text-align:center;font-family:'Roboto Condensed',sans-serif;font-size:23px;color:#666;text-transform:uppercase}
.welcome-title b{font-size:28px;font-weight:400;color:var(--blue)}
.welcome-intro{position:absolute;left:100px;top:58px;width:696px;text-align:center;font-size:13.2px;line-height:19px;color:#666}
.service{position:absolute;top:147px;width:219px}
.service-photo{width:219px;height:106px;border:4px solid var(--white);box-shadow:0 1px 3px rgba(0,0,0,.25)}
.service h3{margin-top:13px;font-family:'Roboto Condensed',sans-serif;font-weight:400;font-size:18px;color:var(--green)}
.service p{margin-top:6px;font-size:10.5px;line-height:14px;color:#555}
.service-rule{position:absolute;left:0;top:195px;width:219px;height:1px;background:var(--grey-line)}
.btn-more{position:absolute;left:61px;top:186px;width:84px;height:19px;border:1px solid #c9c9c9;border-radius:10px;background:linear-gradient(#ffffff,#e6e6e6);font-family:'Arimo',sans-serif;font-size:9px;line-height:17px;text-align:center;color:var(--text-dark)}

/* articles */
.section-head{position:absolute;font-family:'Roboto Condensed',sans-serif;font-weight:700;font-size:19px;color:var(--text-dark);text-transform:uppercase}
.section-head em{font-style:normal;color:var(--green)}
.article{position:absolute;left:105px;width:435px}
.article-photo{position:absolute;left:0;top:0;width:83px;height:77px;border:3px solid #e4e4e4;background:linear-gradient(#d9d9d9,#8a8a8a)}
.article h4{position:absolute;left:98px;top:-2px;font-weight:500;font-size:12.5px;color:var(--text-dark)}
.article p{position:absolute;left:98px;top:22px;width:340px;font-size:10.2px;line-height:14px;color:#555}
.article .meta{position:absolute;left:98px;top:64px;font-style:italic;font-size:8.5px;color:#888}
.article .meta span+span{margin-left:26px}
.article-rule{position:absolute;left:105px;top:957px;width:435px;height:1px;background:#e3e3e3}
.btn-all{position:absolute;left:105px;top:1064px;width:424px;height:18px;border-radius:9px;background:#e8e8e8;font-family:'Arimo',sans-serif;font-size:9px;line-height:18px;text-align:right;padding-right:17px;color:var(--text-dark);letter-spacing:.5px}

.side-card{position:absolute;left:589px;width:202px;border:4px solid #ececec;border-radius:3px}

/* footer */
.footer-links{position:absolute;left:0;top:1112px;width:896px;height:58px;border-top:1px solid #dddddd;background:#f7f7f7}
.footer-nav{position:absolute;left:105px;top:22px;font-size:11px;color:#444}
.footer-nav i{font-style:normal;color:#aaa;margin:0 3px}
.social{position:absolute;top:17px;width:27px;height:27px;border-radius:50%}
.copyright-bar{position:absolute;left:0;top:1170px;width:896px;height:30px;background:var(--green);color:var(--white);font-size:11px;line-height:30px}
.copyright-bar .left{position:absolute;left:105px}
.copyright-bar .right{position:absolute;right:105px}
</style>
</head>
<body>

<header class="site-header">
  <svg class="logo-tab" width="440" height="64" viewBox="0 0 440 64">
    <defs><linearGradient id="tabShade" x1="0" y1="0" x2="0" y2="1"><stop offset="0" stop-color="#9ee22c" stop-opacity=".6"/><stop offset="1" stop-color="#3f7a06" stop-opacity=".4"/></linearGradient></defs>
    <path d="M0 0H340C372 0 368 62 410 62H0Z" fill="#6cb212"/>
    <path d="M0 0H340C372 0 368 62 410 62H0Z" fill="url(#tabShade)"/>
  </svg>
  <div class="logo-text">Movara<br>Consultancy</div>
  <nav class="main-nav">
    <span class="n1">HOME</span><span class="n2">ABOUT</span><span class="n3">SERVICES</span><span class="n4">ARTICAL</span><span>CONTACT</span>
  </nav>
</header>

<section class="hero">
  <div class="hero-photo" role="img" aria-label="Monochrome crowd of business people in silhouette with a smiling consultant in a dark suit on the right"></div>
  <div class="hero-title">
    <div class="line1">YOUR <span class="hl">VISION,</span></div>
    <div class="line2">OUR EXPERTISE</div>
  </div>
  <svg class="hero-arrow" width="896" height="352" viewBox="0 0 896 352">
    <defs><linearGradient id="arrowFill" x1="0" y1="-1" x2="0" y2="1"><stop offset="0" stop-color="#96dc22"/><stop offset="1" stop-color="#62ae0c"/></linearGradient></defs>
    <g transform="translate(525 158) rotate(64)">
      <polygon points="-126,0 -66,-62 -66,-38 132,-38 132,38 -66,38 -66,62" fill="url(#arrowFill)" stroke="#a6e23a" stroke-width="1.5"/>
      <line x1="-50" y1="2" x2="124" y2="2" stroke="#ffffff" stroke-opacity=".55" stroke-dasharray="3 3"/>
      <text x="-46" y="-10" font-family="Oswald,sans-serif" font-weight="500" font-size="22" fill="#2f5d02">OUR MANAGEMENT,</text>
      <text x="-78" y="17" font-family="Raleway,sans-serif" font-size="11.5" fill="#ffffff">IT and technology experts are</text>
      <text x="-72" y="31" font-family="Raleway,sans-serif" font-size="11.5" fill="#ffffff">committed to helping you...</text>
    </g>
  </svg>
</section>

<section class="welcome">
  <h1 class="welcome-title">Welcome to <b>Movara Consultancy</b></h1>
  <p class="welcome-intro">Lorem Ipsum is simply dummy text of the printing and typesetting industry. Lorem Ipsum has been the industry's standard dummy text ever since the 1500s, when an unknown printer took a galley of type and scrambled it to make a type specimen book survived not only five centuries.</p>

  <article class="service" style="left:105px">
    <div class="service-photo" role="img" aria-label="Consultant presenting a bar chart to a training group" style="background:linear-gradient(90deg,#4a3a30,#3f5f8e 50%,#c9d2dc)"></div>
    <h3>Financial Training</h3>
    <p>Lorem Ipsum is simply dummy text of the printing and typesetting industry.</p>
    <div class="service-rule"></div><div class="btn-more">VIEW MORE</div>
  </article>
  <article class="service" style="left:338px">
    <div class="service-photo" role="img" aria-label="Accountant reviewing documents at a bright desk" style="background:linear-gradient(90deg,#dfe6ec,#c6cdd6 50%,#e9edf0)"></div>
    <h3>Forensic Accounting</h3>
    <p>Lorem Ipsum is simply dummy text of the printing and typesetting industry.</p>
    <div class="service-rule"></div><div class="btn-more">VIEW MORE</div>
  </article>
  <article class="service" style="left:571px">
    <div class="service-photo" role="img" aria-label="Team of managers meeting in a modern office" style="background:linear-gradient(90deg,#dfe4ea,#9fb0c4 60%,#e6eaee)"></div>
    <h3>Professional Management</h3>
    <p>Lorem Ipsum is simply dummy text of the printing and typesetting industry.</p>
    <div class="service-rule"></div><div class="btn-more">VIEW MORE</div>
  </article>
</section>

<svg class="abs" style="left:106px;top:822px" width="30" height="26" viewBox="0 0 30 26">
  <ellipse cx="12" cy="10" rx="11" ry="8" fill="#7cc614"/><polygon points="6,16 4,22 11,17" fill="#7cc614"/>
  <ellipse cx="20" cy="16" rx="9" ry="6.5" fill="#e86aa8"/><polygon points="24,21 27,25 20,22" fill="#e86aa8"/>
</svg>
<h2 class="section-head" style="left:144px;top:820px">New <em>Article</em></h2>

<article class="article" style="top:865px">
  <div class="article-photo" role="img" aria-label="Portrait of the article author"></div>
  <h4>Lorem Ipsum is simply dummy...</h4>
  <p>Lorem Ipsum is simply dummy text of the printing &amp; typesetting industry, lorem ipsum has been the industry.</p>
  <div class="meta"><span>17 May 2013</span><span>68 Comment</span></div>
</article>
<div class="article-rule"></div>
<article class="article" style="top:972px">
  <div class="article-photo" role="img" aria-label="Portrait of the article author"></div>
  <h4>Lorem Ipsum is simply dummy...</h4>
  <p>Lorem Ipsum is simply dummy text of the printing &amp; typesetting industry, lorem ipsum has been the industry.</p>
  <div class="meta"><span>17 May 2013</span><span>68 Comment</span></div>
</article>
<div class="btn-all">VIEW ALL</div>

<svg class="abs" style="left:590px;top:821px" width="26" height="22" viewBox="0 0 26 22">
  <rect x="1" y="5" width="22" height="15" fill="#f3b23a" stroke="#c98512"/><path d="M1 5L12 14L23 5" fill="none" stroke="#c98512"/>
  <rect x="14" y="1" width="10" height="7" fill="#3a8fd6"/>
</svg>
<h2 class="section-head" style="left:622px;top:820px">Send a <em>Message</em></h2>
<div class="side-card" style="top:853px;height:79px">
  <div role="img" aria-label="Send a message banner with a mailbox and click here button" style="width:100%;height:100%;background:linear-gradient(#2aa0e6,#0e6db5)"></div>
</div>
<div class="side-card" style="top:953px;height:128px">
  <div role="img" aria-label="World map with thumbs-up markers and a row of people silhouettes" style="width:100%;height:100%;background:linear-gradient(#7fd2de,#4ab8c8)"></div>
</div>

<footer>
  <div class="footer-links">
    <div class="footer-nav">Home<i>|</i>About<i>|</i>Services<i>|</i>Subjects<i>|</i>Blog<i>|</i>Sitemap<i>|</i>Terms of Use<i>|</i>Connect with us</div>
    <div class="social" style="left:692px;background:#2f62a8"></div>
    <div class="social" style="left:727px;background:#8a8a8a"></div>
    <div class="social" style="left:762px;background:#8a8a8a"></div>
  </div>
  <div class="copyright-bar">
    <span class="left">Copyright © 2013 Movara Consultancy.&nbsp; All Rights Reserved.</span>
    <span class="right">History | Contact | Privacy</span>
  </div>
</footer>

</body>
</html>
```